Front and back of folded card is black. Front has your logo design in gold ink.Inside panel says Chapel of the Silver Lantern.org Recovery is GoldenBack of card, says Rev. Dr. Zoli Althea Brownegold ink This is for folks facing their shadow work in the recovery process from addictions. I see this: A black dove heading down into an open rose with thorns and a cross.

Target Market(s)

addiction recovery

Contact Information for Business Card

The card will be folded. Outside front panel has logo
Inside panel has copy and back side has copy

Logo Text

Dark purple dove flying into open rose with thorns , include a cross in the design

Font styles to use
Script

Colors
fbed22
6b449b
33a6d7

Requirements
Must have
• Legible script font...beautiful, hopeful, serious.
Should not have
• silly or overdone theme

```html
<!DOCTYPE html>
<html lang="en">
<head>
<meta charset="utf-8">
<title>Chapel of the Silver Lantern – Folded Card</title>
<link rel="stylesheet" href="https://fonts.googleapis.com/css2?family=Pinyon+Script&family=Open+Sans:wght@600&display=swap">
<style>
  :root {
    --backdrop: #c3c7ca;
    --panel-inside: #ffffff;
    --panel-front: #000000;
    --ink-dark: #1a1a1a;
    --ink-grey: #555555;
    --script-silver: #b9b9b9;
    --mark-grey: #d6d6d6;
    --brand-gold: #fbed22;
    --brand-purple: #6b449b;
    --brand-blue: #33a6d7;
  }
  * { box-sizing: border-box; }
  html, body {
    margin: 0;
    padding: 0;
    width: 1200px;
    height: 900px;
    overflow: hidden;
    background: var(--backdrop);
  }
  .spread {
    position: absolute;
    left: 60px;
    top: 270px;
    width: 1080px;
    height: 360px;
    display: flex;
    box-shadow: 0 6px 18px rgba(0,0,0,0.18);
  }
  .panel {
    position: relative;
    width: 540px;
    height: 360px;
    overflow: hidden;
  }
  .panel--inside { background: var(--panel-inside); }
  .panel--front { background: var(--panel-front); }

  .mark-slot {
    position: absolute;
    border-radius: 50%;
  }
  .panel--inside .mark-slot {
    left: 30px;
    top: 40px;
    width: 140px;
    height: 140px;
    background: var(--mark-grey);
  }
  .panel--front .mark-slot {
    left: 360px;
    top: 110px;
    width: 120px;
    height: 120px;
    border: 3px solid var(--brand-gold);
  }

  .inside-copy {
    position: absolute;
    left: 180px;
    right: 30px;
    top: 150px;
    text-align: right;
  }
  .script {
    font-family: "Pinyon Script", cursive;
    font-weight: 400;
    margin: 0;
    white-space: nowrap;
  }
  .inside-site,
  .inside-tagline {
    font-size: 26px;
    line-height: 38px;
    color: var(--ink-grey);
  }
  .signature {
    position: absolute;
    right: 30px;
    bottom: 40px;
    text-align: right;
  }
  .signature-line {
    font-family: "Open Sans", sans-serif;
    font-weight: 600;
    color: var(--ink-dark);
    font-size: 20px;
    line-height: 30px;
    margin: 0;
    white-space: nowrap;
  }

  .front-name {
    position: absolute;
    left: 40px;
    top: 145px;
    font-size: 28px;
    color: var(--script-silver);
  }
</style>
</head>
<body>
  <main class="spread">
    <section class="panel panel--inside" aria-label="Inside panel">
      <div class="mark-slot" role="img" aria-label="Chapel of the Silver Lantern mark area"></div>
      <div class="inside-copy">
        <p class="script inside-site">Chapel of the Silver Lantern.org</p>
        <p class="script inside-tagline">Healing is Silver Back of card</p>
      </div>
      <div class="signature">
        <p class="signature-line">Says Rev.</p>
        <p class="signature-line">Dr. Mirel Danica Fossegold ink</p>
      </div>
    </section>
    <section class="panel panel--front" aria-label="Front panel">
      <p class="script front-name">Chapel of the Silver Lantern</p>
      <div class="mark-slot" role="img" aria-label="Chapel of the Silver Lantern mark area"></div>
    </section>
  </main>
</body>
</html>
```